Federal Research Council Deep Records PI Summit 2016

We need a poster for a FRC-sponsored (Federal Research Council) project presented by Halvermoor University and the University of Westbrook on April 20-21, 2016.

This is what the project will be about: (of course this is something that the audience/participants of this project will understand) The growth in scale, diversity, and complexity of data has increased the demand for understanding large amounts of heterogeneous data. This presents new challenges to the way data and information are used and managed. The goal of the two-day workshop is to bring together PIs and co-PIs currently funded by the Deep Records program at FRC along with selected industry and government invitees to discuss current research, identify current challenges, and discuss promising future directions.

Possible key words to incorporate: data analytics, security, machine learning, social, environment, health, medicine, energy, data visualization, optimization, scalable algorithms, data mining, massive data, privacy, data ethics

The key words we included were for two purposes:

- for data-related graphics ideas (i.e. images of data visualization
graphs or machine learning, etc.)
- or to use some or all of the actual words throughout the poster

- Poster size - Height = 34.5 inches
Width = 27.5 inches

- No contact info needed.

- Date - April 20th-21st (exact time not needed)

- Location - Arlington, VA

- Text - Federal Research Council
Deep Records PI Summit - 2016
April 20th-21st
Arlington, VA

***Federal Research Council and Deep Records PI Summit 2016 need to be
significantly bigger than the other text.

That is the only required text.

We'd like to see the colors that are shades of blue, yellow/gold and (possibly) red.

We've attached the two university logos to incorporate into the design.
- Images/photos – We don’t have photos but will be happy to see data
science-related images. We're open to photos of groups of people showing
diversity; please don't use an image of just one person. If we need to pay
for it, please provide the link for purchase, so we can check it out. Thank
you.

Thank you for submitting your designs. We won't be able to review them until Monday March 28th and will adjust the deadline as needed. Added Saturday, March 26, 2016

Target Market(s)

Researchers and government employees in various disciplines: data science, engineering, mathematics, health, climate, sociology

Industry/Entity Type

University

Font styles to use
Serif

Colors
f04a50
3276b5
fece3e

Requirements
Must have
• FRC DRPI - 2016 Summit
• Arlington, VA
• April 20th-21st
• University logos

```html
<!DOCTYPE html>
<html lang="en">
<head>
<meta charset="utf-8">
<title>Federal Research Council Deep Records PI Summit 2016</title>
<link rel="stylesheet" href="https://fonts.googleapis.com/css2?family=PT+Serif:ital,wght@0,400;0,700;1,400&display=swap">
<style>
  :root {
    --navy: #2b465d;
    --deep-blue: #35607f;
    --sky: #3f8bb5;
    --ink: #16212b;
    --title-grey: #c9ccdc;
    --keyword: #dbeaf3;
    --white: #ffffff;
    --gold: #fece3e;
    --gold-line: #b9a660;
    --red: #f04a50;
    --brand-blue: #3276b5;
  }
  * { margin: 0; padding: 0; box-sizing: border-box; }
  html, body { width: 957px; height: 1200px; overflow: hidden; background: var(--navy); }
  .poster {
    position: relative;
    width: 957px;
    height: 1200px;
    overflow: hidden;
    font-family: "PT Serif", Georgia, serif;
    background:
      radial-gradient(ellipse 620px 760px at 120px 760px, rgba(80,170,215,0.55), rgba(80,170,215,0) 70%),
      linear-gradient(200deg, #2a4058 0%, #33607f 45%, #3a7aa2 75%, #2f5c7c 100%);
  }
  .backdrop { position: absolute; inset: 0; }
  .watermark-word {
    position: absolute;
    left: 345px;
    top: -20px;
    font-size: 150px;
    font-weight: 400;
    color: rgba(255,255,255,0.12);
    transform-origin: left top;
    transform: rotate(90deg) translate(0, -150px);
    letter-spacing: 6px;
    white-space: nowrap;
  }
  .council {
    position: absolute;
    left: 62px;
    top: 70px;
    font-size: 40px;
    font-weight: 400;
    color: var(--ink);
    white-space: nowrap;
  }
  .program {
    position: absolute;
    left: 60px;
    top: 114px;
    font-size: 74px;
    font-weight: 700;
    color: var(--title-grey);
    white-space: nowrap;
    line-height: 1.1;
  }
  .summit {
    position: absolute;
    right: 563px;
    top: 214px;
    font-size: 40px;
    font-weight: 700;
    color: var(--white);
    white-space: nowrap;
  }
  .year {
    position: absolute;
    left: 430px;
    top: 214px;
    font-size: 40px;
    font-weight: 700;
    color: var(--title-grey);
  }
  .keywords {
    position: absolute;
    right: 565px;
    top: 273px;
    list-style: none;
    text-align: right;
    font-size: 22px;
    line-height: 29px;
    color: var(--keyword);
  }
  .event-details {
    position: absolute;
    left: 429px;
    top: 274px;
    font-size: 22px;
    line-height: 34px;
    color: var(--ink);
  }
  .event-details sup { font-size: 12px; }
  .presenters-label {
    position: absolute;
    left: 424px;
    top: 992px;
    font-size: 20px;
    font-style: italic;
    color: var(--ink);
  }
  .presenter {
    position: absolute;
    top: 1048px;
    width: 82px;
    height: 91px;
    background: var(--white);
    display: flex;
    align-items: center;
    justify-content: center;
    text-align: center;
    padding: 6px;
    font-size: 11px;
    line-height: 1.25;
    color: var(--ink);
  }
  .presenter--westbrook { left: 429px; }
  .presenter--halvermoor { left: 519px; }
</style>
</head>
<body>
<main class="poster">
  <svg class="backdrop" width="957" height="1200" viewBox="0 0 957 1200" aria-hidden="false">
    <defs>
      <radialGradient id="globe-tone" cx="0.55" cy="0.5" r="0.55">
        <stop offset="0" stop-color="#6fb3c3" stop-opacity="0.75"/>
        <stop offset="0.7" stop-color="#4f95ad" stop-opacity="0.45"/>
        <stop offset="1" stop-color="#3a6f8c" stop-opacity="0"/>
      </radialGradient>
      <linearGradient id="wave-tone" x1="0" y1="0" x2="1" y2="1">
        <stop offset="0" stop-color="#7fd4f0" stop-opacity="0.45"/>
        <stop offset="1" stop-color="#3aa0d0" stop-opacity="0.1"/>
      </linearGradient>
      <radialGradient id="glow-gold">
        <stop offset="0" stop-color="#fece3e"/>
        <stop offset="0.45" stop-color="#fece3e" stop-opacity="0.85"/>
        <stop offset="1" stop-color="#fece3e" stop-opacity="0"/>
      </radialGradient>
      <radialGradient id="glow-red">
        <stop offset="0" stop-color="#f04a50"/>
        <stop offset="0.45" stop-color="#f04a50" stop-opacity="0.85"/>
        <stop offset="1" stop-color="#f04a50" stop-opacity="0"/>
      </radialGradient>
    </defs>

    <circle cx="880" cy="640" r="470" fill="url(#globe-tone)" role="img" aria-label="Globe of the Americas linked by a data network"/>
    <path d="M0 260 C120 520 260 800 420 1200 L0 1200 Z" fill="url(#wave-tone)" role="img" aria-label="Glowing wireframe data wave"/>

    <line x1="62" y1="206" x2="872" y2="206" stroke="var(--gold-line)" stroke-width="2"/>
    <circle cx="872" cy="206" r="22" fill="url(#glow-gold)"/>

    <line x1="412" y1="136" x2="412" y2="750" stroke="var(--red)" stroke-width="2" stroke-opacity="0.75"/>
    <circle cx="412" cy="750" r="18" fill="url(#glow-red)"/>

    <line x1="384" y1="1032" x2="880" y2="1032" stroke="var(--gold-line)" stroke-width="2"/>
    <circle cx="880" cy="1032" r="22" fill="url(#glow-gold)"/>
  </svg>

  <div class="watermark-word" aria-hidden="true">data</div>

  <h1 class="council">Federal Research Council</h1>
  <p class="program">Deep Records</p>
  <p class="summit">PI Summit</p>
  <p class="year">2016</p>

  <ul class="keywords">
    <li>data analytics</li>
    <li>security</li>
    <li>machine learning</li>
    <li>social</li>
    <li>environment</li>
    <li>health</li>
    <li>medicine</li>
    <li>energy</li>
    <li>data visualization</li>
    <li>optimization</li>
    <li>scalable algorithms</li>
    <li>data mining</li>
    <li>massive data</li>
    <li>privacy</li>
    <li>data ethics</li>
  </ul>

  <p class="event-details">April 20<sup>th</sup>-21<sup>st</sup><br>Arlington VA</p>

  <p class="presenters-label">presented by</p>
  <div class="presenter presenter--westbrook">University of Westbrook</div>
  <div class="presenter presenter--halvermoor">Halvermoor University</div>
</main>
</body>
</html>
```